Property Service business needs a cool business card

Looking for an eloquent and unique business card using the logo and colours attached as uploaded files.

Target Market(s)

Body corporates, real estate agents, building managers

Industry/Entity Type

Business

Contact Information for Business Card

- Quorvel Logo
- Construction * Maintenance * Remedial

- Tom Wexley
- Business Manager

- Ph 0417586204
- P.O Box 461 South Melbourne Vic 3090
- Email tom@quorvel.com
- Website www.quorvelpropertyservices.com.au

Requirements
Must have
• Clean and fresh look, colours must be vibrant!
Nice to have
• unique features
Should not have
• Should not be overcrowded

```html
<!DOCTYPE html>
<html lang="en">
<head>
<meta charset="utf-8">
<title>Quorvel Business Card</title>
<link rel="stylesheet" href="https://fonts.googleapis.com/css2?family=Source+Sans+3:wght@400;600;700&display=swap">
<style>
  :root {
    --backdrop: #1b1b1b;
    --card-light: #e9eaec;
    --card-blue: #0e57a6;
    --brand-blue: #1a5aa6;
    --brand-green: #8cc63f;
    --text-dark: #3c3c3c;
    --white: #ffffff;
  }
  * { margin: 0; padding: 0; box-sizing: border-box; }
  html, body {
    width: 1200px; height: 900px; overflow: hidden;
    background: var(--backdrop);
    font-family: "Source Sans 3", sans-serif;
  }
  .canvas { position: relative; width: 1200px; height: 900px; }
  .card {
    position: absolute; width: 432px; height: 250px; border-radius: 12px;
  }
  .card-front { left: 153px; top: 309px; background: var(--card-light); }
  .card-back { left: 631px; top: 311px; background: var(--card-blue); }

  .brand { position: absolute; display: flex; align-items: center; gap: 10px; }
  .brand-mark { width: 50px; height: 50px; background: var(--brand-green); }
  .brand-name { font-size: 30px; font-weight: 400; letter-spacing: 0.5px; line-height: 1; }
  .card-front .brand { left: 28px; top: 97px; }
  .card-front .brand-name { color: var(--brand-blue); }
  .card-back .brand { left: 106px; top: 94px; }
  .card-back .brand-mark { width: 60px; height: 60px; }
  .card-back .brand-name { color: var(--white); font-size: 34px; }

  .details { position: absolute; left: 229px; top: 46px; color: var(--text-dark); }
  .person-name { font-size: 19.5px; font-weight: 700; color: var(--brand-blue); line-height: 24px; }
  .person-role { font-size: 12.5px; line-height: 16px; }
  .address { margin-top: 10px; font-size: 12.5px; line-height: 14px; }
  .contacts { margin-top: 11px; list-style: none; font-size: 12.5px; }
  .contacts li { display: flex; align-items: center; height: 16.2px; }
  .contacts svg { width: 9px; height: 9px; margin-right: 8px; fill: var(--brand-blue); flex: none; }
</style>
</head>
<body>
<main class="canvas">
  <section class="card card-front">
    <div class="brand">
      <span class="brand-mark"></span>
      <span class="brand-name">Quorvel</span>
    </div>
    <div class="details">
      <p class="person-name">Tom Wexley</p>
      <p class="person-role">Managing Director</p>
      <p class="address">1234, Address Goes Here<br>Country Name, 123456</p>
      <ul class="contacts">
        <li><svg viewBox="0 0 10 10"><path d="M2.5 0h5v10h-5z M3.5 1v7h3V1z" fill-rule="evenodd"/></svg>123-456-7890</li>
        <li><svg viewBox="0 0 10 10"><path d="M0 3c0-2 10-2 10 0v1H7V3H3v1H0z M1.5 5h7l1 4h-9z"/></svg>123-456-7890</li>
        <li><svg viewBox="0 0 10 10"><path d="M2 0h5v3H2z M0 3h10v7H0z M1 5h3v1H1z"/></svg>123-456-7890</li>
        <li><svg viewBox="0 0 10 10"><path d="M0 2h10v6H0z M0 2l5 3.5L10 2" /></svg>info@quorvel.com</li>
        <li><svg viewBox="0 0 10 10"><path d="M1 7l3-3 1 1-3 3z M5 3l2-2 2 2-2 2-1-1 1-1-.5-.5-1 1z"/></svg>www.quorvel.com</li>
      </ul>
    </div>
  </section>

  <section class="card card-back">
    <div class="brand">
      <span class="brand-mark"></span>
      <span class="brand-name">Quorvel</span>
    </div>
  </section>
</main>
</body>
</html>
```